I need a Facebook, Instagram post, for Outdoor Training
I need my logo,
Business name : Valmora Soccer Academy
Boys and girls Outdoor Soccer training
Passing, Kicking Shooting, Dribbling, Ball Control
Field: Brookvale Turf #5(1746 Hollowmere Lane Dunstead, MD 20419)
Time: 5:30pm-6:30pm 5-8 years old
6;30pm-7:30pm 9-12 years old
7:30pm-8:30pm 13-18 years old
Registration $210 ( Includes 1st month, registration, practice uniform)

Register online:
www.valmoraacademy.example
Phone:(240)555-0187

Target Market(s)

YOUTH KIDS

Colors
0054AA
0677BA
7BADD7
CADEEF
E8F1F8

Requirements
Must have
• blue , or black and white

```html
<!DOCTYPE html>
<html lang="en">
<head>
<meta charset="utf-8">
<title>Valmora Soccer Academy – Outdoor Soccer Training</title>
<link rel="stylesheet" href="https://fonts.googleapis.com/css2?family=Russo+One&family=Montserrat:ital,wght@0,400;0,500;0,600;0,700;1,800;1,900&family=Oswald:wght@400;500&display=swap">
<style>
  :root {
    --blue-deep: #0054AA;
    --blue-mid: #0677BA;
    --blue-bright: #1a8be6;
    --blue-soft: #7BADD7;
    --blue-pale: #CADEEF;
    --blue-mist: #E8F1F8;
    --black: #000000;
    --white: #ffffff;
    --stage: #bfbfbf;
    --sky: #3f5c78;
    --turf: #1f2a24;
  }
  * { box-sizing: border-box; margin: 0; padding: 0; }
  html, body { width: 1195px; height: 1200px; overflow: hidden; background: var(--stage); }
  .post {
    position: absolute; left: 0; top: 2px; width: 1195px; height: 1195px;
    overflow: hidden; background: var(--black);
    font-family: "Montserrat", Arial, sans-serif; color: var(--white);
  }
  .backdrop {
    position: absolute; left: 0; top: 0; width: 1195px; height: 880px;
    background: linear-gradient(180deg, #4a6784 0%, #3c5873 30%, #2b435a 48%, #26332d 54%, var(--turf) 100%);
  }
  .players {
    position: absolute; left: 590px; top: 245px; width: 605px; height: 720px;
    background: radial-gradient(ellipse at 45% 55%, rgba(6,119,186,.75) 0%, rgba(123,173,215,.45) 45%, rgba(0,84,170,0) 75%);
  }
  .shapes { position: absolute; left: 0; top: 0; }
  .headline {
    position: absolute; left: 78px; font-family: "Russo One", sans-serif;
    line-height: 1; text-transform: uppercase;
    background: linear-gradient(180deg, #ffffff 0%, #e6e6e6 45%, #a9a9a9 100%);
    -webkit-background-clip: text; background-clip: text; color: transparent;
    -webkit-text-stroke: 3px var(--blue-deep);
    filter: drop-shadow(0 3px 3px rgba(0,0,0,.45));
  }
  .headline--boys { top: 80px; font-size: 150px; letter-spacing: -2px; }
  .headline--and { left: 585px; top: 126px; font-size: 86px; }
  .headline--girls { top: 218px; font-size: 150px; letter-spacing: -2px; }
  .training-band {
    position: absolute; left: 0; top: 371px; width: 1195px; height: 128px;
    background: linear-gradient(90deg, var(--blue-deep) 0%, var(--blue-deep) 55%, rgba(0,84,170,.35) 100%);
  }
  .training-title {
    position: absolute; left: 76px; top: 378px; font-family: "Montserrat", sans-serif;
    font-weight: 900; font-style: italic; font-size: 44px; line-height: 50px;
    text-transform: uppercase; letter-spacing: 1px;
  }
  .skills { position: absolute; left: 78px; top: 525px; list-style: none; }
  .skills li {
    display: flex; align-items: center; height: 64.5px;
    font-weight: 800; font-style: italic; font-size: 37px; letter-spacing: 1px;
  }
  .skills svg { width: 26px; height: 26px; margin-right: 24px; flex: none; }
  .brand {
    position: absolute; left: 925px; top: 105px; width: 210px; text-align: center;
    font-family: "Montserrat", sans-serif; font-weight: 800; font-size: 24px; line-height: 28px;
    color: var(--white); text-transform: uppercase;
  }
  .register-label { position: absolute; left: 80px; top: 832px; font-weight: 500; font-size: 30px; }
  .url {
    position: absolute; left: 82px; top: 891px; font-family: "Oswald", sans-serif;
    font-weight: 400; font-size: 45px; line-height: 56px; letter-spacing: -1px; transform: scaleX(.93); transform-origin: left;
  }
  .url-note { position: absolute; left: 82px; top: 953px; font-size: 18.5px; font-weight: 500; letter-spacing: .3px; }
  .price {
    position: absolute; left: 632px; top: 865px; width: 166px; height: 116px;
    background: var(--blue-deep); border-radius: 8px;
    font-family: "Oswald", sans-serif; font-weight: 500; font-size: 84px; line-height: 116px; text-align: center;
  }
  .price sup { font-size: 36px; vertical-align: 34px; margin-right: 2px; }
  .schedule { position: absolute; left: 82px; top: 998px; list-style: none; }
  .schedule li { display: flex; align-items: center; height: 50px; }
  .schedule svg { width: 22px; height: 22px; margin-right: 12px; }
  .schedule .time { font-family: "Oswald", sans-serif; font-size: 31px; width: 206px; letter-spacing: -.5px; }
  .schedule .age { font-family: Arial, sans-serif; font-weight: 700; font-size: 22px; color: var(--blue-bright); }
  .divider { position: absolute; left: 531px; top: 1012px; width: 2px; height: 122px; background: var(--white); }
  .venue { position: absolute; left: 570px; top: 1006px; }
  .venue-name { font-size: 46px; font-weight: 600; line-height: 52px; white-space: nowrap; }
  .venue-name .label { font-size: 33px; font-weight: 500; color: var(--blue-bright); }
  .venue-address { font-size: 19.5px; font-weight: 500; margin-top: 4px; white-space: nowrap; }
  .phone { font-size: 43px; font-weight: 700; margin-top: 8px; white-space: nowrap; }
  .phone span { color: var(--blue-bright); }
</style>
</head>
<body>
<main class="post">
  <div class="backdrop" role="img" aria-label="Photo of an outdoor soccer stadium with palm trees, goal and turf field"></div>
  <div class="players" role="img" aria-label="Photo of a girl and a boy in blue soccer kits, the boy holding a soccer ball"></div>

  <svg class="shapes" width="1195" height="1195" viewBox="0 0 1195 1195" aria-hidden="true">
    <polygon points="392,0 1195,0 1195,118 1090,126 945,128" fill="var(--blue-deep)"/>
    <polygon points="392,0 412,0 945,126 1195,118 1195,138 938,142" fill="var(--black)"/>
    <polygon points="0,821 600,821 620,836 1195,948 1195,970 620,881 0,881" fill="rgba(0,84,170,.55)"/>
    <polygon points="0,881 620,881 800,888 1195,966 1195,1195 0,1195" fill="var(--black)"/>
    <line x1="800" y1="888" x2="1195" y2="966" stroke="var(--white)" stroke-width="2.5"/>
    <line x1="388" y1="851" x2="620" y2="851" stroke="var(--white)" stroke-width="2.5"/>
  </svg>

  <div class="brand">Valmora Soccer Academy</div>

  <h1>
    <span class="headline headline--boys">Boys</span>
    <span class="headline headline--and">and</span>
    <span class="headline headline--girls">Girls</span>
  </h1>

  <div class="training-band"></div>
  <h2 class="training-title">Outdoor Soccer<br>Training</h2>

  <ul class="skills">
    <li><svg viewBox="0 0 26 26"><circle cx="13" cy="13" r="12" fill="var(--white)"/><path d="M7.5 13.5l4 3.5 7-8" stroke="var(--black)" stroke-width="3" fill="none" stroke-linecap="round" stroke-linejoin="round"/></svg>PASSING</li>
    <li><svg viewBox="0 0 26 26"><circle cx="13" cy="13" r="12" fill="var(--white)"/><path d="M7.5 13.5l4 3.5 7-8" stroke="var(--black)" stroke-width="3" fill="none" stroke-linecap="round" stroke-linejoin="round"/></svg>KICKING SHOOTING</li>
    <li><svg viewBox="0 0 26 26"><circle cx="13" cy="13" r="12" fill="var(--white)"/><path d="M7.5 13.5l4 3.5 7-8" stroke="var(--black)" stroke-width="3" fill="none" stroke-linecap="round" stroke-linejoin="round"/></svg>DRIBBLING</li>
    <li><svg viewBox="0 0 26 26"><circle cx="13" cy="13" r="12" fill="var(--white)"/><path d="M7.5 13.5l4 3.5 7-8" stroke="var(--black)" stroke-width="3" fill="none" stroke-linecap="round" stroke-linejoin="round"/></svg>BALL CONTROL</li>
  </ul>

  <p class="register-label">Register online:</p>
  <p class="url">WWW.VALMORAACADEMY.EXAMPLE</p>
  <p class="url-note">Includes 1st month, registration, practice uniform</p>
  <div class="price"><sup>$</sup>210</div>

  <ul class="schedule">
    <li><svg viewBox="0 0 22 22"><circle cx="11" cy="11" r="9.5" fill="none" stroke="var(--blue-bright)" stroke-width="2" stroke-dasharray="50 4"/><path d="M11 5.5V11l4 2.5" stroke="var(--blue-bright)" stroke-width="2" fill="none"/></svg><span class="time">5:30PM-6:30PM</span><span class="age">5-8 years old</span></li>
    <li><svg viewBox="0 0 22 22"><circle cx="11" cy="11" r="9.5" fill="none" stroke="var(--blue-bright)" stroke-width="2" stroke-dasharray="50 4"/><path d="M11 5.5V11l4 2.5" stroke="var(--blue-bright)" stroke-width="2" fill="none"/></svg><span class="time">6;30PM-7:30PM</span><span class="age">9-12 years old</span></li>
    <li><svg viewBox="0 0 22 22"><circle cx="11" cy="11" r="9.5" fill="none" stroke="var(--blue-bright)" stroke-width="2" stroke-dasharray="50 4"/><path d="M11 5.5V11l4 2.5" stroke="var(--blue-bright)" stroke-width="2" fill="none"/></svg><span class="time">7:30PM-8:30PM</span><span class="age">13-18 years old</span></li>
  </ul>

  <div class="divider"></div>

  <div class="venue">
    <p class="venue-name"><span class="label">Field:</span> Brookvale Turf #5</p>
    <p class="venue-address">(1746 Hollowmere Lane Dunstead, MD 20419)</p>
    <p class="phone">Call Us:<span>(240)555-0187</span></p>
  </div>
</main>
</body>
</html>
```